South Carolina Bridal and Formal Wear Store

We want The Gown Parlor of Marlowe website to feel luxurious, elegant, welcoming, and approachable—without feeling overpriced or intimidating. The site should immediately show that we are a full-service bridal and formal wear destination, offering bridal gowns, prom, mothers’ dresses, tuxedos and suits, accessories, and more. We want beautiful, high-end imagery and a clean, modern design while still reflecting the warm, personal experience customers receive when they walk into our boutique. Most importantly, the website should be easy to shop and navigate, allowing customers to browse our collections, see what we offer, understand price ranges, book appointments, and feel excited and comfortable choosing The Gown Parlor of Marlowe for all of their special-event needs.

Target Market(s)

Women ages 18-50. Brides, engaged women, mothers of the occasion

Industry/Entity Type

Bridal and Formal Wear

Coding

Coded - Design and coding required

Number of Pages Required

5+ page

Font styles to use
Sans Serif

Colors

Designer to choose colors to be used in the design.

Requirements
Must have
• Appointment area, about us staff area, what we offer and designers our logo
Nice to have
• Modern Southern Luxury: Clean, elegant, and upscale with soft neutral tones, beautiful bridal photography, and a warm Lowcountry feel.
Should not have
• pricing

```html
<!DOCTYPE html>
<html lang="en">
<head>
<meta charset="utf-8">
<title>Contact · The Gown Parlor of Marlowe</title>
<link href="https://fonts.googleapis.com/css2?family=Bricolage+Grotesque:wght@500;600&family=Inter:wght@400;500;600&display=swap" rel="stylesheet">
<style>
  :root{
    --cream:#f6f1ea;
    --cream-line:#e6ddd2;
    --ink:#221c19;
    --ink-soft:#4a413c;
    --rust:#b0552f;
    --rust-dim:#4a2a1d;
    --card-text:#f3ece4;
    --photo-a:#8a7a6c;
    --photo-b:#b8aca0;
    --map:#e7eee6;
  }
  *{box-sizing:border-box;margin:0;padding:0}
  html,body{width:883px;height:1200px;overflow:hidden}
  body{position:relative;background:var(--cream);font-family:"Inter",sans-serif;color:var(--ink)}
  .abs{position:absolute}
  .display{font-family:"Bricolage Grotesque",sans-serif;font-weight:500;letter-spacing:-0.02em}
  .eyebrow{font-size:5.6px;letter-spacing:.22em;text-transform:uppercase;color:var(--rust);font-weight:500}

  .topbar{left:0;top:0;width:883px;height:15px;background:var(--ink);color:#d8cfc6;font-size:5.8px}
  .topbar span{position:absolute;top:4px;display:flex;align-items:center;gap:3px}
  .topbar svg{width:6px;height:6px}

  .brand{left:341px;top:30px;width:200px;text-align:center;font-size:12.5px;font-weight:500;color:var(--ink);letter-spacing:.01em}
  .btn{display:flex;align-items:center;justify-content:center;color:#fff;font-weight:600;background:var(--rust)}
  .header-book{left:621px;top:30px;width:96px;height:22px;font-size:5.6px}
  .header-rule{left:166px;top:68px;width:551px;height:1px;background:var(--cream-line)}
  .nav{left:0;top:76px;width:883px;font-size:6.4px;letter-spacing:.06em;color:var(--ink)}
  .nav a{position:absolute;color:inherit;text-decoration:none}
  .nav a.current{border-bottom:1px solid var(--ink);padding-bottom:2px}

  .hero-photo{left:441px;top:92px;width:442px;height:323px;background:linear-gradient(135deg,var(--photo-a),var(--photo-b) 55%,#7d8a64)}
  .visit-tag{left:822px;top:382px;width:46px;height:18px;background:var(--ink);color:#fff;font-size:5.8px;letter-spacing:.08em;font-weight:600}
  .hero-title{left:29px;top:216px;font-size:27px;line-height:1.05}
  .hero-copy{left:29px;top:283px;width:250px;font-size:7.4px;line-height:1.6;color:var(--ink-soft)}

  .info-card{left:166px;top:460px;width:211px;height:357px;background:var(--ink);color:var(--card-text)}
  .info-card .num{position:absolute;left:18px;top:18px;font-size:24px;color:var(--rust-dim);font-family:"Bricolage Grotesque",sans-serif}
  .info-card .eyebrow{position:absolute;left:18px;font-size:5.2px;letter-spacing:.14em}
  .info-card p{position:absolute;left:18px;font-size:7.6px;line-height:1.6}
  .info-card a{color:inherit;text-decoration:underline;text-decoration-color:var(--rust);text-underline-offset:2px}
  .hours{position:absolute;left:18px;width:147px;font-size:6.6px;line-height:1.8}
  .hours div{display:flex;justify-content:space-between}
  .map{position:absolute;left:18px;top:237px;width:175px;height:102px;background:var(--map)}

  .form-card{left:393px;top:460px;width:324px;height:359px;background:var(--cream);border:1px solid var(--cream-line);box-shadow:0 8px 20px rgba(34,28,25,.06)}
  .form-card .eyebrow{position:absolute;left:18px;top:20px}
  .form-card h2{position:absolute;left:18px;top:34px;font-size:11px;font-weight:400}
  .form-card .lead{position:absolute;left:18px;top:52px;width:285px;font-size:7.3px;line-height:1.5;color:var(--ink-soft)}
  .label{position:absolute;font-size:5.6px;letter-spacing:.12em;color:var(--ink-soft)}
  .field{position:absolute;border:1px solid var(--cream-line);background:var(--cream);font-size:7.6px;display:flex;align-items:center;padding:0 8px;justify-content:space-between}
  .send{position:absolute;left:18px;top:315px;width:87px;height:25px;background:var(--ink);color:#fff;font-size:7.2px;font-weight:600;letter-spacing:.04em}

  .cta{left:0;top:864px;width:883px;height:118px;background:var(--ink)}
  .cta h2{position:absolute;left:166px;top:36px;font-size:21.5px;line-height:1.02;color:#fff}
  .cta-book{left:600px;top:55px;width:117px;height:25px;font-size:7.4px}

  .footer{left:0;top:982px;width:883px;height:218px;background:var(--ink);border-top:1px solid #3a322d;color:#d8cfc6}
  .footer .brand-foot{position:absolute;left:166px;top:33px;font-size:9.5px;font-weight:500;color:#fff}
  .footer p,.footer li{font-size:6.8px;line-height:1.5}
  .footer ul{list-style:none}
  .footer .eyebrow{position:absolute;font-size:6px;letter-spacing:.14em}
  .footer .legal{position:absolute;top:203px;font-size:5.6px;color:#b9aea4}
  .footer .rule{position:absolute;left:0;top:188px;width:883px;height:1px;background:#3a322d}
</style>
</head>
<body>

<div class="abs topbar">
  <span style="left:166px"><svg viewBox="0 0 10 10" fill="none" stroke="#b0552f"><rect x="1" y="2" width="8" height="7"/><path d="M1 4h8"/></svg>Wed – Sat, 10am – 6pm · Marlowe, SC</span>
  <span style="left:522px"><svg viewBox="0 0 10 10" fill="none" stroke="#b0552f"><path d="M2 1l2 2-1 1.5a6 6 0 0 0 2.5 2.5L7 6l2 2-1.5 1.5C4 9 1 6 .5 2.5z"/></svg>555-214-0188</span>
  <span style="left:582px"><svg viewBox="0 0 10 10" fill="none" stroke="#b0552f"><rect x="1" y="2" width="8" height="6"/><path d="M1 2l4 3 4-3"/></svg>appointments@thegownparlorofmarlowe.com</span>
</div>

<div class="abs brand">The Gown Parlor of Marlowe</div>
<a class="abs btn header-book">Book an Appointment</a>
<div class="abs header-rule"></div>
<nav class="abs nav">
  <a style="left:305px">HOME</a>
  <a style="left:343px">ABOUT</a>
  <a style="left:384px">COLLECTIONS</a>
  <a style="left:447px">APPOINTMENTS</a>
  <a style="left:517px">FAQ</a>
  <a class="current" style="left:548px">CONTACT</a>
</nav>

<div class="abs eyebrow" style="left:29px;top:203px">Contact</div>
<h1 class="abs display hero-title">We'd love to hear<br>from you</h1>
<p class="abs hero-copy">Visit our boutique in the heart of Marlowe, or reach out any time — we're happy to help.</p>
<div class="abs hero-photo" role="img" aria-label="Bride and groom leaving a rustic barn ceremony under a shower of petals"></div>
<div class="abs btn visit-tag">VISIT US</div>

<section class="abs info-card">
  <div class="num">01</div>
  <div class="eyebrow" style="top:64px">Visit the Boutique</div>
  <p style="top:79px">220 Magnolia Row, Suite 4<br>Marlowe, SC 29000</p>
  <div class="eyebrow" style="top:119px">Reach Us</div>
  <p style="top:133px">Phone: <a>555-214-0188</a><br>Email:<br><a>appointments@thegownparlorofmarlowe.com</a></p>
  <div class="eyebrow" style="top:186px">Store Hours</div>
  <div class="hours" style="top:198px">
    <div><span>Sunday – Tuesday</span><span>Closed</span></div>
    <div><span>Wednesday – Saturday</span><span>10am – 6pm</span></div>
  </div>
  <div class="map" role="img" aria-label="Street map showing the boutique location"></div>
</section>

<section class="abs form-card">
  <div class="eyebrow">Get in Touch</div>
  <h2>Request an Appointment or Ask a Question</h2>
  <p class="lead">Fill out the form below and our team will follow up to confirm your appointment details.</p>
  <div class="label" style="left:18px;top:89px">FULL NAME</div>
  <div class="field" style="left:18px;top:100px;width:138px;height:22px"></div>
  <div class="label" style="left:167px;top:89px">EMAIL</div>
  <div class="field" style="left:167px;top:100px;width:138px;height:22px"></div>
  <div class="label" style="left:18px;top:134px">PHONE</div>
  <div class="field" style="left:18px;top:145px;width:138px;height:22px"></div>
  <div class="label" style="left:167px;top:134px">APPOINTMENT TYPE</div>
  <div class="field" style="left:167px;top:145px;width:138px;height:22px"><span>VIP Bridal Appointment</span><svg width="6" height="4" viewBox="0 0 6 4"><path d="M.5.5L3 3 5.5.5" fill="none" stroke="#221c19"/></svg></div>
  <div class="label" style="left:18px;top:179px">PREFERRED DATE</div>
  <div class="field" style="left:18px;top:190px;width:287px;height:22px"><span>dd-mm-yyyy</span><svg width="7" height="7" viewBox="0 0 10 10"><rect x="1" y="2" width="8" height="7" fill="none" stroke="#221c19" stroke-width="1.4"/><path d="M1 4h8" stroke="#221c19" stroke-width="1.4"/></svg></div>
  <div class="label" style="left:18px;top:224px">MESSAGE</div>
  <div class="field" style="left:18px;top:235px;width:287px;height:67px"></div>
  <div class="btn send">Send Request</div>
</section>

<section class="abs cta">
  <h2 class="display">Ready to say yes to the<br>dress?</h2>
  <a class="abs btn cta-book">Book an Appointment</a>
</section>

<footer class="abs footer">
  <div class="brand-foot">The Gown Parlor of Marlowe</div>
  <p style="position:absolute;left:166px;top:66px;width:145px;line-height:1.55">A full-service bridal &amp; formal wear boutique bringing modern Southern luxury to Marlowe, SC.</p>
  <div class="eyebrow" style="left:166px;top:121px">Store Hours</div>
  <div style="position:absolute;left:166px;top:138px;width:124px;font-size:6.8px;line-height:1.75">
    <div style="display:flex;justify-content:space-between"><span>Sun – Tue</span><span>Closed</span></div>
    <div style="display:flex;justify-content:space-between"><span>Wed – Sat</span><span>10am – 6pm</span></div>
  </div>
  <div class="eyebrow" style="left:403px;top:31px">Explore</div>
  <ul style="position:absolute;left:403px;top:47px;line-height:2.2">
    <li style="line-height:2.2">About Us</li><li style="line-height:2.2">Collections</li><li style="line-height:2.2">Appointments</li><li style="line-height:2.2">FAQ</li>
  </ul>
  <div class="eyebrow" style="left:498px;top:31px">Visit Us</div>
  <p style="position:absolute;left:498px;top:47px">220 Magnolia Row, Suite 4<br>Marlowe, SC 29000</p>
  <p style="position:absolute;left:498px;top:72px">555-214-0188</p>
  <p style="position:absolute;left:498px;top:87px">appointments@thegownparlorofmarlowe.com</p>
  <div class="rule"></div>
  <div class="legal" style="left:166px">© 2026 The Gown Parlor of Marlowe. All rights reserved.</div>
  <div class="legal" style="right:166px">Bridal · Tuxedos · Formal Wear · Marlowe, SC</div>
</footer>

</body>
</html>
```